New Stationary and Logo Design for Start Up Company

We need a logo design and stationary set including letterhead, business card (double sided), compliments slip and envelope for a new company Bright Quill Media.
The files should be editable to update address and standard contact details, will need to forward to web designer and stationary printer.
The company will be an online marketer and distributer of various business education products in Australia.
The designs should convey simple clean image
Target Market(s)
Small business owners and professional service providers (ie Accountants, Lawyers, Real Estate Agents) in Australia
Industry/Entity Type
Education
Look and feel
Each slider illustrates characteristics of the customer's brand and the style your logo design should communicate.

```html
<!DOCTYPE html>
<html lang="en">
<head>
<meta charset="utf-8">
<title>Bright Quill Media – Envelope</title>
<link rel="stylesheet" href="https://fonts.googleapis.com/css2?family=Open+Sans:wght@400;600;700&display=swap">
<style>
  :root {
    --brand-blue: #1076bf;
    --white: #ffffff;
    --ink: #1d1d1f;
    --window-fill: #e9e9ea;
    --window-stroke: #4a4a4a;
    --decor-tint: #dfe9f0;
    --decor-edge: #e6e3ef;
    --metal-a: #d8d8dc;
    --metal-b: #f3f3f5;
    --metal-c: #b9b3bd;
  }
  * { box-sizing: border-box; margin: 0; padding: 0; }
  html, body { width: 1200px; height: 514px; overflow: hidden; background: var(--white); }
  body { font-family: "Open Sans", Arial, sans-serif; color: var(--ink); }

  .envelope { position: relative; width: 1200px; height: 514px; overflow: hidden; background: var(--white); }

  .header-band {
    position: absolute; left: 0; top: 0; width: 1200px; height: 79px;
    background: var(--brand-blue); color: var(--white);
    padding: 15px 0 0 15px;
  }
  .header-address { font-size: 12px; line-height: 16px; }
  .header-contact { font-size: 17px; line-height: 24px; margin-top: 4px; }
  .header-contact .label { font-weight: 700; margin-right: 4px; }
  .header-contact .web { font-weight: 700; margin-left: 14px; }

  .metal-band {
    position: absolute; left: 0; top: 79px; width: 1200px; height: 30px;
    background: linear-gradient(90deg, var(--metal-a) 0%, var(--metal-c) 22%, var(--metal-b) 42%, var(--metal-a) 58%, var(--metal-c) 74%, var(--metal-b) 88%, var(--metal-a) 100%);
  }

  .decor-area {
    position: absolute; left: 0; top: 109px; width: 190px; height: 270px;
    background: linear-gradient(135deg, var(--decor-tint) 0%, var(--decor-edge) 55%, var(--white) 100%);
  }

  .address-window {
    position: absolute; left: 45px; top: 384px; width: 533px; height: 104px;
    background: var(--window-fill); border: 1px solid var(--window-stroke); border-radius: 12px;
  }

  .brand-lockup {
    position: absolute; left: 762px; top: 352px; width: 224px;
    text-align: center; color: var(--ink); font-weight: 600;
  }
  .brand-mark { display: block; width: 70px; height: 70px; margin: 0 auto 8px; border-radius: 50%; background: var(--brand-blue); }
  .brand-name { font-size: 21px; line-height: 26px; letter-spacing: 1px; text-transform: uppercase; }

  .web-tab {
    position: absolute; left: 998px; top: 434px; width: 202px; height: 35px;
    background: var(--brand-blue); color: var(--white);
    font-size: 18px; line-height: 35px; padding-left: 20px;
  }
</style>
</head>
<body>
  <div class="envelope">
    <header class="header-band">
      <p class="header-address">Bright Quill Media Ltd&nbsp; Unit 4807, Level 3&nbsp; 012-345 Harbour Lane, Newtown, NSW 2042</p>
      <p class="header-contact"><span class="label">T:</span>01234 567 8000<span class="web">www.brightquillmedia.com</span></p>
    </header>

    <div class="metal-band"></div>

    <div class="decor-area" role="img" aria-label="Soft pale blue decorative background graphic"></div>

    <div class="address-window"></div>

    <div class="brand-lockup">
      <span class="brand-mark"></span>
      <p class="brand-name">Bright Quill<br>Media</p>
    </div>

    <div class="web-tab">www.quillpress.com</div>
  </div>
</body>
</html>
```